Business Card design for amazing new Dental Office

Please read this brief closely!

Our client is a modern new dental office/
They love their new logo.
Now it's time to create a business card for them.

It should be a two sided card:
Side one should have the logo and name and maybe a color background or design.
Side two should have all the contact information which is here:

Marcus Pellow, D.D.S
General and Cosmetic Dentistry
4178 W. Orchard Lane
Ventura, CA 93017
(805) 219-4862
drmarc@bluefernsmiles.example
www.bluefernsmiles.example

Feel free to arrange that info as you like and to style both sides of the card according to your creativity. This is a chance for you to show your design skills!

Client is open to font choices and is looking for a style that is amazing and premium. Colors can be selected from the logo, or any variation of those.

You will not win this contest with a less than beautiful card design so please feel free to make multiple submissions.

Logo files attached and please message me with any questions.
Thanks!

Target Market(s)

Families and Professionals seeking dental services

Industry/Entity Type

Dental

Contact Information for Business Card

Logo, style, contact info as per the brief

Font styles to use
Sans Serif

Requirements
Must have
• Client's logo and contact details as per brief
Nice to have
• Unique style reflecting high end dental clinic near the beach
Should not have
• Must not look like a template

```html
<!DOCTYPE html>
<html lang="en">
<head>
<meta charset="utf-8">
<title>Blue Fern Smiles – Business Card</title>
<link href="https://fonts.googleapis.com/css2?family=Josefin+Sans:wght@300;400&family=Arimo:wght@400&display=swap" rel="stylesheet">
<style>
  :root {
    --page: #e4e5e6;
    --white: #ffffff;
    --teal: #6cc2bc;
    --sky: #6ac3dc;
    --ocean: #48b3e7;
    --grey-type: #9c9c9c;
  }
  * { margin: 0; padding: 0; box-sizing: border-box; }
  html, body { width: 1200px; height: 900px; overflow: hidden; }
  body { background: var(--page); position: relative; }

  .card {
    position: absolute;
    top: 216px;
    width: 309px;
    height: 501px;
    border-radius: 155px 155px 0 0;
    overflow: hidden;
    text-align: center;
  }
  .card--front { left: 279px; }
  .card--back { left: 617px; }

  .card__bands { position: absolute; inset: 0; width: 100%; height: 100%; }

  .brand-dot {
    position: absolute;
    left: 50%;
    width: 44px;
    height: 44px;
    margin-left: -22px;
    border-radius: 50%;
  }
  .card--front .brand-dot { top: 190px; background: var(--white); }
  .card--back .brand-dot { top: 72px; background: var(--teal); }

  .brand-name {
    position: absolute;
    left: 0;
    right: 0;
    font-family: "Josefin Sans", sans-serif;
    font-weight: 300;
    text-transform: uppercase;
    line-height: 1;
  }
  .brand-name__main { display: block; font-size: 34px; letter-spacing: 2px; }
  .brand-name__sub { display: block; font-size: 16px; letter-spacing: 11px; margin-top: 10px; padding-left: 11px; }
  .card--front .brand-name { top: 276px; color: var(--white); }
  .card--back .brand-name { top: 160px; color: var(--grey-type); }

  .dentist { position: absolute; left: 0; right: 0; top: 273px; color: var(--white); }
  .dentist__name { font-family: "Josefin Sans", sans-serif; font-weight: 400; font-size: 20px; line-height: 1; }
  .dentist__role { font-family: "Arimo", sans-serif; font-size: 13.5px; margin-top: 4px; }

  .contact-icons {
    position: absolute; left: 0; right: 0; top: 346px;
    display: flex; justify-content: center; align-items: center; gap: 3px;
  }
  .contact-icons__rule { width: 46px; height: 1px; background: rgba(255,255,255,0.7); margin: 0 5px; }
  .contact-icons__box {
    width: 22px; height: 21px; background: var(--white); border-radius: 2px;
    display: flex; align-items: center; justify-content: center;
  }

  .contact-lines, .address {
    position: absolute; left: 0; right: 0; color: var(--white);
    font-family: "Arimo", sans-serif; font-size: 13.5px; line-height: 17.5px;
  }
  .contact-lines { top: 371px; }
  .address { top: 448px; line-height: 17px; }
</style>
</head>
<body>

<section class="card card--front" aria-label="Card front">
  <svg class="card__bands" viewBox="0 0 309 501" preserveAspectRatio="none" aria-hidden="true">
    <defs>
      <filter id="soften-front" x="-10%" y="-10%" width="120%" height="120%">
        <feGaussianBlur stdDeviation="5"/>
      </filter>
    </defs>
    <rect width="309" height="501" fill="var(--ocean)"/>
    <g filter="url(#soften-front)">
      <path d="M-20 -20 H329 V300 Q154 324 -20 300 Z" fill="var(--sky)"/>
      <path d="M-20 -20 H329 V156 Q154 192 -20 156 Z" fill="var(--teal)"/>
    </g>
  </svg>
  <span class="brand-dot"></span>
  <h1 class="brand-name">
    <span class="brand-name__main">Blue Fern</span>
    <span class="brand-name__sub">Smiles</span>
  </h1>
</section>

<section class="card card--back" aria-label="Card back">
  <svg class="card__bands" viewBox="0 0 309 501" preserveAspectRatio="none" aria-hidden="true">
    <defs>
      <filter id="soften-back" x="-10%" y="-10%" width="120%" height="120%">
        <feGaussianBlur stdDeviation="4"/>
      </filter>
    </defs>
    <rect width="309" height="501" fill="var(--white)"/>
    <path d="M0 232 Q154 272 309 236 V501 H0 Z" fill="var(--teal)"/>
    <g filter="url(#soften-back)">
      <path d="M-20 320 Q154 342 329 316 V520 H-20 Z" fill="var(--sky)"/>
      <path d="M-20 418 Q154 442 329 414 V520 H-20 Z" fill="var(--ocean)"/>
    </g>
  </svg>

  <span class="brand-dot"></span>
  <h2 class="brand-name">
    <span class="brand-name__main">Blue Fern</span>
    <span class="brand-name__sub">Smiles</span>
  </h2>

  <div class="dentist">
    <p class="dentist__name">Marcus Pellow, D.D.S</p>
    <p class="dentist__role">General and Cosmetic Dentistry</p>
  </div>

  <div class="contact-icons" aria-hidden="true">
    <span class="contact-icons__rule"></span>
    <span class="contact-icons__box">
      <svg width="14" height="12" viewBox="0 0 14 12"><path d="M1 4 Q7 0 13 4 L11 5 L10 3.5 Q7 2.5 4 3.5 L3 5 Z" fill="var(--sky)"/><path d="M4 6 H10 L11.5 11 H2.5 Z" fill="var(--sky)"/><circle cx="7" cy="8.3" r="1.4" fill="var(--white)"/></svg>
    </span>
    <span class="contact-icons__box">
      <svg width="14" height="10" viewBox="0 0 14 10"><rect x="0.5" y="0.5" width="13" height="9" fill="none" stroke="var(--sky)"/><path d="M0.5 0.5 L7 6 L13.5 0.5 M0.5 9.5 L5 5 M13.5 9.5 L9 5" fill="none" stroke="var(--sky)"/></svg>
    </span>
    <span class="contact-icons__box">
      <svg width="14" height="14" viewBox="0 0 14 14"><circle cx="7" cy="7" r="6.5" fill="var(--sky)"/><path d="M4 4 Q6 3 7 5 Q6 7 8 8 Q9 10 7 12 Q4 10 5 8 Q3 7 4 4 Z" fill="var(--white)"/></svg>
    </span>
    <span class="contact-icons__rule"></span>
  </div>

  <div class="contact-lines">
    <p>(805) 219-4862</p>
    <p>drmarc@bluefernsmiles.example</p>
    <p>www.bluefernsmiles.example</p>
  </div>

  <address class="address" style="font-style: normal;">
    <p>4178 W. Orchard Lane</p>
    <p>Ventura, CA 93017</p>
  </address>
</section>

</body>
</html>
```